Fast-casual chicken restaurant Plume Rally needs a catering menu design

We need a catering menu designed for Plume Rally. We are looking to design a 24x36in landscape menu board for our new catering menu. The catering memo attached includes our catering menu and Plume Rally branding. More information about our brand can be found at https://plumerally.example/.

```html
<!DOCTYPE html>
<html lang="en">
<head>
<meta charset="utf-8">
<title>Plume Rally Catering Menu</title>
<link href="https://fonts.googleapis.com/css2?family=Montserrat:wght@600;700;800;900&display=swap" rel="stylesheet">
<style>
:root{
  --backdrop:#5d6d87;
  --brand-yellow:#fccc2c;
  --brand-red:#d63b2a;
  --cream:#fdf9e3;
  --slate:#5b6b8c;
  --charcoal:#5e5e5e;
  --ink:#5a5a5a;
  --name-blue:#4f6290;
  --rule:#7a7a7a;
}
*{box-sizing:border-box;margin:0;padding:0}
html,body{width:1200px;height:1200px;overflow:hidden;background:var(--backdrop)}
body{font-family:"Montserrat",sans-serif;position:relative}
.menu-board{
  position:absolute;left:30px;top:220px;width:1763px;height:1175px;
  transform:scale(0.6466);transform-origin:0 0;overflow:hidden;
  background:linear-gradient(to bottom,var(--brand-yellow) 0 590px,var(--brand-red) 590px 100%);
}
.photo{position:absolute}
.photo-wings-platter{left:-20px;top:-120px;width:495px;height:300px;border-radius:50%;background:radial-gradient(circle at 55% 60%,#d49a48,#9b5b22 60%,#3e3e42 75%)}
.photo-dip{left:580px;top:-50px;width:115px;height:112px;border-radius:50%;background:radial-gradient(circle,#eef0e6 55%,#2b2b2b 58%)}
.photo-ribs{left:830px;top:-40px;width:240px;height:237px;border-radius:45%;background:radial-gradient(circle at 50% 45%,#7a2a18,#4a1a10 50%,#1f1f1f 62%)}
.photo-tenders{left:1595px;top:0;width:168px;height:367px;border-radius:12px 0 0 12px;background:radial-gradient(circle at 55% 50%,#c8802e,#a9581f 55%,#f1efe9 80%)}
.photo-onion-rings{left:0;top:512px;width:115px;height:295px;border-radius:0 40px 40px 0;background:radial-gradient(circle at 30% 50%,#d9a04e,#b97830 60%,#262626 85%)}
.photo-hot-tenders{left:325px;top:1022px;width:310px;height:310px;border-radius:50%;background:radial-gradient(circle at 50% 40%,#c8402a,#8a2a1a 55%,#2a2a2a 75%)}
.photo-ketchup{left:1095px;top:1092px;width:85px;height:85px;border-radius:50%;background:radial-gradient(circle,#b81a1a 55%,#cfcfcf 60%,#8a8a8a 75%)}
.photo-waffle-fries{left:1210px;top:997px;width:260px;height:260px;border-radius:50%;background:radial-gradient(circle,#e39a3a,#c97a26 60%,#b8b8b8 80%)}
.photo-mustard{left:1620px;top:1137px;width:80px;height:80px;border-radius:50%;background:radial-gradient(circle,#e9b940 55%,#f4f0e4 62%)}

.menu-panel{position:absolute;left:147px;top:109px;width:1468px;height:958px;background:var(--cream)}

.section-title{
  position:absolute;height:55px;font-weight:900;font-size:41px;line-height:55px;
  color:#fff;padding:0 14px;letter-spacing:0.5px;white-space:nowrap;
}
.title-packaged{left:303px;top:142px;width:430px;background:var(--brand-yellow)}
.title-per-person{left:1013px;top:142px;width:467px;background:var(--slate)}
.title-carte{left:373px;top:562px;width:290px;background:var(--charcoal)}
.title-sauces{left:1127px;top:562px;width:206px;background:var(--brand-red)}

.menu-table{
  position:absolute;border-collapse:collapse;table-layout:fixed;
  border:1.5px solid var(--rule);color:var(--ink);
}
.menu-table th{
  height:42px;font-weight:800;font-size:20px;border-left:1.5px solid var(--rule);
  border-bottom:1.5px solid var(--rule);text-align:center;vertical-align:middle;
}
.menu-table td{
  font-weight:700;font-size:19px;line-height:20.5px;text-align:center;vertical-align:top;
  border-left:1.5px solid var(--rule);padding:0 4px;
}
.menu-table .name-head{color:var(--name-blue)}
.menu-table tr.pad td{height:9px;padding:0}
.deals-table{top:199px;width:705px;height:344px}
.packaged-table{left:165px}
.per-person-table{left:893px}
.deals-table td{font-weight:600}
.deals-table td.label{font-weight:700}
.deals-table tr.row-a td{height:82px}
.deals-table tr.row-b td{height:102px}
.carte-table{left:165px;top:618px;width:705px;height:414px}
.sauce-table{left:893px;top:618px;width:705px;height:414px}
.carte-table tr.single td{height:41px}
.carte-table tr.double td{height:61px}
.sauce-table tr.sauce-row td{height:61px}
.menu-table tr.fill td{height:auto}
</style>
</head>
<body>
<main class="menu-board" aria-label="Plume Rally catering menu">
  <div class="photo photo-wings-platter" role="img" aria-label="Platter of assorted sauced and dry-rubbed wings"></div>
  <div class="photo photo-dip" role="img" aria-label="Cup of ranch dressing"></div>
  <div class="photo photo-ribs" role="img" aria-label="Tray of barbecue ribs"></div>
  <div class="photo photo-tenders" role="img" aria-label="Tray of fried chicken tenders"></div>
  <div class="photo photo-onion-rings" role="img" aria-label="Basket of onion rings"></div>
  <div class="photo photo-hot-tenders" role="img" aria-label="Plate of spicy sauced tenders"></div>
  <div class="photo photo-ketchup" role="img" aria-label="Cup of ketchup"></div>
  <div class="photo photo-waffle-fries" role="img" aria-label="Basket of waffle fries"></div>
  <div class="photo photo-mustard" role="img" aria-label="Cup of honey mustard"></div>

  <div class="menu-panel"></div>

  <h2 class="section-title title-packaged">PACKAGED DEALS</h2>
  <table class="menu-table deals-table packaged-table">
    <colgroup><col style="width:138px"><col style="width:104px"><col style="width:219px"><col style="width:117px"><col></colgroup>
    <tr><th class="name-head" style="border-left:none">NAME</th><th>FEEDS</th><th>ITEMS</th><th>PRICE</th><th>CALORIES</th></tr>
    <tr class="pad"><td style="border-left:none"></td><td></td><td></td><td></td><td></td></tr>
    <tr class="row-a"><td class="label" style="border-left:none">FAMILY</td><td>4</td><td>12 tenders, sauces.<br>dressing, large<br>side, 2L</td><td class="label">$24.99</td><td></td></tr>
    <tr class="row-b"><td class="label" style="border-left:none">TAILGATE</td><td>10</td><td>20 tenders,<br>30 wings, sauces,<br>dressings,<br>1 party side</td><td class="label">$75.99</td><td></td></tr>
    <tr class="fill"><td class="label" style="border-left:none">HOUSE<br>PARTY</td><td>10</td><td>20 tenders,<br>60 wings, sauces,<br>2 party sides,<br>2 party slads,<br>dressings, 2 2L</td><td class="label">$155.99</td><td></td></tr>
  </table>

  <h2 class="section-title title-per-person">PER PERSON DEALS</h2>
  <table class="menu-table deals-table per-person-table">
    <colgroup><col style="width:137px"><col style="width:104px"><col style="width:219px"><col style="width:117px"><col></colgroup>
    <tr><th style="border-left:none">NAME</th><th>FEEDS</th><th>ITEMS</th><th>PRICE</th><th>CALORIES</th></tr>
    <tr class="pad"><td style="border-left:none"></td><td></td><td></td><td></td><td></td></tr>
    <tr class="row-a"><td class="label" style="border-left:none">SNACK<br>(per person)</td><td>1</td><td>2 tenders, sauce,<br>dressing,<br>1 reg side</td><td class="label">$7.00</td><td></td></tr>
    <tr class="row-b"><td class="label" style="border-left:none">PARTY<br>(per person)</td><td>1</td><td>2 tenders,<br>3 wings, sauce,<br>dressing, 1 reg side,<br>12/oz fountain drink</td><td class="label">$11.00</td><td></td></tr>
    <tr class="fill"><td class="label" style="border-left:none">FEAST<br>(per person)</td><td>1</td><td>2 tenders,<br>6 wings, sauce,<br>dressing, 1 reg side,<br>dessert, 20/oz drink</td><td class="label">$15.00</td><td></td></tr>
  </table>

  <h2 class="section-title title-carte">A LA CARTE</h2>
  <table class="menu-table carte-table">
    <colgroup><col style="width:193px"><col style="width:193px"><col style="width:192px"><col></colgroup>
    <tr><th style="border-left:none">ITEMS</th><th>INCREMENTS</th><th>PRICE</th><th>CALORIES</th></tr>
    <tr class="pad"><td style="border-left:none"></td><td></td><td></td><td></td></tr>
    <tr class="single"><td style="border-left:none">WINGS</td><td>50, 75, 100</td><td>$</td><td></td></tr>
    <tr class="single"><td style="border-left:none">TENDERS</td><td>30, 45, 60</td><td>$</td><td></td></tr>
    <tr class="single"><td style="border-left:none">WAFFLE FRIES</td><td>PARTY SIZE</td><td>$13.99</td><td></td></tr>
    <tr class="double"><td style="border-left:none">GARLIC<br>PARM TOTS</td><td>PARTY SIZE</td><td>$13.99</td><td></td></tr>
    <tr class="double"><td style="border-left:none">CHICKEN<br>CEASAR SALAD</td><td>PARTY SIZE</td><td>$38.99</td><td></td></tr>
    <tr class="single"><td style="border-left:none">CEASAR SALAD</td><td>PARTY SIZE</td><td>$27.99</td><td></td></tr>
    <tr class="single"><td style="border-left:none">ANY SAUCE</td><td>8 OZ</td><td>$1.99</td><td></td></tr>
    <tr class="fill"><td style="border-left:none">CHEESE SAUCE</td><td>8 OZ</td><td>$2.49</td><td></td></tr>
  </table>

  <h2 class="section-title title-sauces">SAUCES</h2>
  <table class="menu-table sauce-table">
    <colgroup><col style="width:143px"><col style="width:139px"><col style="width:140px"><col style="width:147px"><col></colgroup>
    <tr><th style="border-left:none">FLAVORS</th><th>BBQ</th><th>DRY RUBS</th><th>TERIYAKI</th><th>BUFFALO</th></tr>
    <tr class="pad"><td style="border-left:none"></td><td></td><td></td><td></td><td></td></tr>
    <tr class="sauce-row"><td style="border-left:none">HONEY<br>MUSTARD</td><td>CAJUN<br>BBQ</td><td>7 PEPPER</td><td>CAJUN<br>TERIYAKI</td><td>MELLOW</td></tr>
    <tr class="sauce-row"><td style="border-left:none">HOT LEMON<br>PEPPER</td><td>CITRUS<br>CHIPOTLE</td><td>CAJUN</td><td>SPICY<br>TERIYAKI</td><td>STEADY<br>SIMMER</td></tr>
    <tr class="sauce-row"><td style="border-left:none">JAMAICAN<br>JERK</td><td>GOLDEN<br>BBQ</td><td>GARLIC<br>PARM</td><td>TRADITIONAL<br>TERIYAKI</td><td>RED<br>HOT</td></tr>
    <tr class="sauce-row"><td style="border-left:none">MANGO<br>HABANERO</td><td>HONEY<br>BBQ</td><td>LEMON<br>PEPPER</td><td></td><td>HOT COAL</td></tr>
    <tr class="fill"><td style="border-left:none">SWEET<br>CHILI</td><td>KICKIN<br>BBQ</td><td>WEST TEXAS<br>MESQUITE</td><td></td><td>FULL<br>BLAZE</td></tr>
  </table>
</main>
</body>
</html>
```